The Marisol & Jocelyn Fruit Co.

We produce a very high quality freeze dried fruit, all organic, no preservative, no additives, nothing but the fruit. To get more use out of a facility we have in Charlotte, we decided to pursue some high end online retailers with a high end freeze dried organic fruit. We are looking for a very high end, upper east side, trendy, hip, logo and package design for this. There are 4 SKU's - Freeze Dried Strawberries, Freeze Dried Blueberries, Freeze Dried Cherries, and a blend of of all 3 as the 4th SKU. 2 labels each that are 6" x 6" - The front, again needs to be fun and trendy big bold etc. Nothing frilly and Quiet Barn by the creek. The back needs to contain the nutritional statements for each and some copy describing the product and the company.
Updates
This would be one of only a few competitors in this segment
We are looking to steal a page from the wine industry. The coolest looking label on the shelf wins over the uneducated wine buyer. The designs are all fine, but they need to be sleeker, sexier, funner, etc. Someone should look at the label and say....wow that is FUN AND SEXY! I have to buy some! VORBEX.COM screams that. Don't worry so much about pictures of the fruit as the bag is going to be clear. Sell the brand not the fruit. OK?
Reason: Why not?
Reason: Final Selection by Monday 5pm EST.
For all designs that have not been eliminated:
Reason: Final selections. All four designs front and back on one file uploaded by noon tomorrow ( 12:01 PM EST New York)
Target Market(s)
People that would shop at sites like www.vorbex.com
Industry/Entity Type
It Company
Requirements
Nice to have
- The brand is named after our two daughters - One is very girly and the other is very "sassy" It would be fun to have the logo capture their personalities a little. I have uploaded a picture. Marisol on the left, Jocelyn on the right.
Also, another of our brands, Hank Pellow, packaging is attached here. Some consistency in look and feel may be good.
Should not have
- Nothing frilly or dainty, or delicate. Colorful fun and bold but trendy.

```html
<!DOCTYPE html>
<html lang="en">
<head>
<meta charset="utf-8">
<title>The Marisol &amp; Jocelyn Fruit Co. – Freeze Dried Blend Label</title>
<link rel="stylesheet" href="https://fonts.googleapis.com/css2?family=Righteous&family=Poiret+One&family=Limelight&family=Oswald:wght@600&family=Arimo&display=swap">
<style>
  :root {
    --olive: #8a9a2a;
    --red: #e21b2b;
    --crimson: #b3173f;
    --cherry: #c41a3a;
    --purple: #4a2f91;
    --lavender: #7a55a5;
    --orange: #f0921e;
    --ink: #1a1a1a;
    --paper: #ffffff;
  }
  * { margin: 0; padding: 0; box-sizing: border-box; }
  html, body { width: 1200px; height: 1200px; overflow: hidden; background: var(--paper); }
  .label {
    position: relative;
    width: 1200px;
    height: 1200px;
    background: var(--paper);
    border: 2px solid var(--ink);
    overflow: hidden;
  }
  .label > * { position: absolute; line-height: 1; white-space: nowrap; }

  /* Vertical tagline */
  .tagline {
    left: 130px;
    top: 45px;
    transform-origin: top left;
    transform: rotate(90deg);
    color: var(--purple);
    font-size: 78px;
    letter-spacing: 4px;
  }
  .tagline__light { font-family: "Poiret One", sans-serif; font-weight: 400; }
  .tagline__bold {
    display: inline-block;
    font-family: "Righteous", sans-serif;
    transform-origin: left center;
    transform: scaleX(0.64);
    margin-right: -80px;
  }
  .tagline__dots {
    font-family: "Righteous", sans-serif;
    letter-spacing: 8px;
  }

  /* Brand headline */
  .brand { left: 0; top: 0; width: 1200px; height: 0; font-weight: 400; }
  .brand > span { position: absolute; line-height: 1; white-space: nowrap; }
  .brand-the {
    left: 216px; top: 110px;
    font-family: "Righteous", sans-serif;
    font-size: 66px; letter-spacing: 4px;
    color: var(--olive);
  }
  .brand-first {
    left: 380px; top: 92px;
    font-family: "Righteous", sans-serif;
    font-size: 148px; letter-spacing: 4px;
    color: var(--red);
    transform-origin: left top;
    transform: scaleX(0.8);
  }
  .brand-amp {
    left: 972px; top: 10px;
    font-family: "Limelight", sans-serif;
    font-size: 240px;
    color: var(--purple);
  }
  .brand-second {
    left: 214px; top: 242px;
    font-family: "Righteous", sans-serif;
    font-size: 142px; letter-spacing: 4px;
    color: var(--crimson);
    transform-origin: left top;
    transform: scaleX(0.87);
  }
  .brand-co {
    left: 804px; top: 258px;
    font-family: "Righteous", sans-serif;
    font-size: 74px; letter-spacing: 4px;
    color: var(--orange);
    transform-origin: left top;
    transform: scaleX(0.88);
  }

  /* Product name */
  .product-kind {
    left: 214px; top: 502px;
    font-family: "Righteous", sans-serif;
    font-size: 34px; letter-spacing: 3px;
    color: var(--olive);
  }
  .product-name {
    font-family: "Poiret One", sans-serif;
    font-variant: small-caps;
    font-size: 86px;
    letter-spacing: 4px;
  }
  .product-name--line1 { left: 506px; top: 478px; }
  .product-name--line2 { right: 56px; top: 590px; }
  .fruit-blue { color: var(--purple); }
  .fruit-red { color: var(--cherry); }
  .fruit-amp { color: var(--lavender); font-family: "Limelight", sans-serif; font-variant: normal; font-size: 70px; }

  /* Promise panel */
  .promise {
    left: 215px; top: 655px;
    width: 272px; height: 560px;
    background: var(--lavender);
    color: var(--paper);
    font-family: "Oswald", sans-serif;
    font-weight: 600;
    padding: 18px 0 0 18px;
    white-space: normal;
  }
  .promise__claims { list-style: none; font-size: 27px; line-height: 54px; letter-spacing: 0.5px; }
  .promise__note { margin-top: 48px; font-size: 38px; line-height: 53px; }

  /* Fruit illustration area */
  .fruit-art {
    left: 548px; top: 705px;
    width: 340px; height: 462px;
  }

  /* Net weight and footer mark */
  .net-weight {
    left: 917px; top: 1152px;
    font-family: "Arimo", sans-serif;
    font-size: 21px;
    color: var(--ink);
  }
  .footer-mark {
    left: 998px; top: 1100px;
    width: 160px;
    font-family: "Righteous", sans-serif;
    font-size: 27px;
    line-height: 34px;
    color: var(--crimson);
    white-space: normal;
  }
</style>
</head>
<body>
  <main class="label">
    <p class="tagline"><span class="tagline__light">NOTHING BUT THE </span><span class="tagline__bold">FRUIT</span><span class="tagline__dots">..........</span></p>

    <h1 class="brand">
      <span class="brand-the">THE</span>
      <span class="brand-first">MARISOL</span>
      <span class="brand-amp">&amp;</span>
      <span class="brand-second">JOCELYN</span>
      <span class="brand-co">FRUIT CO.</span>
    </h1>

    <span class="product-kind">FREEZE DRIED</span>
    <p class="product-name product-name--line1"><span class="fruit-blue">Blueberries,</span> <span class="fruit-red">Cherries</span></p>
    <p class="product-name product-name--line2"><span class="fruit-amp">&amp;</span> <span class="fruit-red">Strawberries</span></p>

    <section class="promise">
      <ul class="promise__claims">
        <li>ALL ORGANICS</li>
        <li>NO PRESERVATIVES</li>
        <li>NO ADDITIVES</li>
      </ul>
      <p class="promise__note">From<br>our<br>family<br>to<br>yours</p>
    </section>

    <svg class="fruit-art" viewBox="0 0 340 462" role="img" aria-label="Illustration of a blueberry, a cherry and a strawberry over a purple-to-green swirl ring">
      <defs>
        <radialGradient id="fruitTones" cx="50%" cy="55%" r="60%">
          <stop offset="0%" stop-color="#b3173f"/>
          <stop offset="45%" stop-color="#7a3f9a"/>
          <stop offset="80%" stop-color="#3a6fa8"/>
          <stop offset="100%" stop-color="#2a9a7a"/>
        </radialGradient>
      </defs>
      <ellipse cx="170" cy="250" rx="166" ry="205" fill="url(#fruitTones)" opacity="0.85"/>
    </svg>

    <span class="net-weight">1 OZ</span>
    <p class="footer-mark">Marisol &amp; Jocelyn</p>
  </main>
</body>
</html>
```